Menu Design for Indian Restaurant

We are a new Indian restaurant, named Spices of Sarani Restaurant, looking for a sophisticated looking menu. It is a semi-formal dining restaurant with wooden tables and chairs and will have a focus on a creating a lively atmosphere. Environment-friendly products will be used, and the menu will be 100% vegetarian. There will be an emphasis on fresh, healthy and delicious food. We will be targeting vegans, vegetarians, health conscious people, people from all age groups, Indians, Australian's as well as other ethnic communities. We need a clean, simple, sophisticated design for the new restaurant menu. Attached is the restaurant logo for reference.

UPDATE:
- We have attached the menu
- We are not looking for any particular type of layout or size (open to suggests). Please suggest this after having a look at the menu contents. However, we will be having one formal menu to be used in the restaurant, and one in brochure form for distribution.
- There are no images at present. If you feel the need of images, please use sample images for now.

Thank you for the entries thus far.
Updates

Target Market(s)

All age groups from different nationalities

Industry/Entity Type

Indian Restaurant

Colors

Designer to choose colors to be used in the design.

Requirements
Nice to have
• This will be printed on environmentally friendly paper.

```html
<!DOCTYPE html>
<html lang="en">
<head>
<meta charset="utf-8">
<title>Spices of Sarani Restaurant – Menu</title>
<link rel="stylesheet" href="https://fonts.googleapis.com/css2?family=Oswald:wght@500;700&family=Crimson+Pro:wght@300;400&display=swap">
<style>
  :root {
    --paper: #ffffff;
    --ink: #2a2a2a;
    --ink-soft: #3d3d3d;
    --heading-green: #1f7a3a;
    --wash-green: #bfe0b0;
    --wash-mint: #a9d3bd;
    --wash-yellow: #f8e29a;
    --wash-orange: #f7b98a;
    --wash-red: #f19a8f;
    --sketch-grey: #d9d9d9;
  }
  * { margin: 0; padding: 0; box-sizing: border-box; }
  html, body { width: 848px; height: 1200px; overflow: hidden; background: var(--paper); }
  .menu {
    position: relative;
    width: 848px;
    height: 1200px;
    overflow: hidden;
    background:
      radial-gradient(ellipse 260px 420px at 40px 980px, rgba(241,154,143,.55), transparent 70%),
      radial-gradient(ellipse 320px 300px at 220px 880px, rgba(248,226,154,.6), transparent 70%),
      radial-gradient(ellipse 260px 260px at 120px 640px, rgba(247,185,138,.35), transparent 70%),
      radial-gradient(ellipse 380px 320px at 660px 1080px, rgba(169,211,189,.75), transparent 70%),
      radial-gradient(ellipse 300px 380px at 800px 200px, rgba(191,224,176,.7), transparent 70%),
      radial-gradient(ellipse 240px 260px at 760px 560px, rgba(191,224,176,.45), transparent 70%),
      var(--paper);
    font-family: "Crimson Pro", Georgia, serif;
    color: var(--ink);
  }
  .brand {
    position: absolute;
    top: 108px;
    left: 0;
    width: 848px;
    text-align: center;
    z-index: 2;
    font-family: "Oswald", "Arial Narrow", sans-serif;
    font-weight: 500;
    color: #111;
    line-height: 1;
  }
  .brand-name { font-size: 30px; letter-spacing: .5px; }
  .brand-sub { font-size: 10px; letter-spacing: 3px; margin-top: 4px; }
  .hero-art {
    position: absolute;
    top: 70px;
    left: 0;
    width: 848px;
    height: 380px;
    background: linear-gradient(180deg, rgba(217,217,217,0) 0%, rgba(200,200,200,.55) 35%, rgba(190,190,190,.6) 75%, rgba(217,217,217,.15) 100%);
  }
  .section-title {
    position: absolute;
    left: 0;
    width: 848px;
    text-align: center;
    font-family: "Oswald", "Arial Narrow", sans-serif;
    font-weight: 700;
    font-size: 26px;
    line-height: 1;
    color: var(--heading-green);
    letter-spacing: .3px;
  }
  .section-note {
    position: absolute;
    left: 0;
    width: 848px;
    text-align: center;
    font-family: "Oswald", "Arial Narrow", sans-serif;
    font-weight: 500;
    font-size: 12px;
    line-height: 18px;
    color: #111;
  }
  .column { position: absolute; width: 330px; }
  .column.left { left: 57px; }
  .column.right { left: 479px; width: 340px; }
  .dish { margin-bottom: 5px; }
  .dish-name {
    font-size: 15px;
    line-height: 17px;
    font-weight: 400;
    color: var(--ink);
    text-transform: uppercase;
  }
  .dish-name .price, .dish-name .qty { font-size: 11.5px; }
  .dish-desc {
    font-size: 14px;
    line-height: 16.8px;
    font-weight: 300;
    color: var(--ink-soft);
    padding-left: 15px;
  }
</style>
</head>
<body>
<main class="menu">
  <div class="hero-art" role="img" aria-label="Pencil sketch of an Indian palace courtyard with a large burger illustration in the centre"></div>

  <header class="brand">
    <div class="brand-name">Spices of Sarani</div>
    <div class="brand-sub">RESTAURANT</div>
  </header>

  <h2 class="section-title" style="top:448px">BURGER PARADE</h2>
  <p class="section-note" style="top:474px">SERVE WITH SPICY POTATOES FRY'S SARANIEATS.COM</p>
  <div class="column left" style="top:510px">
    <div class="dish"><div class="dish-name">Grass Hopper <span class="price">7.9</span></div>
      <div class="dish-desc">Vegetables potatoes patty beetroot carrot onion lettuce</div></div>
  </div>
  <div class="column right" style="top:510px">
    <div class="dish"><div class="dish-name">Cheese Hopper <span class="price">7.9</span></div>
      <div class="dish-desc">Potato cottage cheese patty tomato capsicum cucumber lettuce cheese</div></div>
  </div>

  <h2 class="section-title" style="top:573px">PIZZA</h2>
  <p class="section-note" style="top:601px">MEDIUM SIZE</p>
  <div class="column left" style="top:638px">
    <div class="dish"><div class="dish-name">Tropicana <span class="price">11.9</span></div>
      <div class="dish-desc">Pineapple capsicum marjoram pitted black olive tomato cheese</div></div>
  </div>
  <div class="column right" style="top:638px">
    <div class="dish"><div class="dish-name">Mexicana <span class="price">12.9</span></div>
      <div class="dish-desc">Jalapeño capsicum tomato mushrooms black olive cheese</div></div>
  </div>

  <h2 class="section-title" style="top:710px">DAKSHANI DHUM</h2>
  <p class="section-note" style="top:737px">SERVING WITH SAMBAR (LENTIL) COCONUT CHUTNEY<br>AND TOMATO CHILLI CHUTNEY</p>

  <div class="column left" style="top:793px">
    <div class="dish"><div class="dish-name">Rava Dosa <span class="price">10.9</span></div>
      <div class="dish-desc">Crispy crepe made with ground rice and lentils gluten free</div></div>
    <div class="dish"><div class="dish-name">Erulli Rava Dosa <span class="price">11.9</span></div>
      <div class="dish-desc">Crispy crepe made with ground rice and lentil stuffed with potatoes</div></div>
    <div class="dish"><div class="dish-name">Plain Dosa <span class="price">10.9</span></div>
      <div class="dish-desc">Crispy crepe made with rice and lentil batter with clarified butter</div></div>
    <div class="dish"><div class="dish-name">Udupi Masala Dosa <span class="price">11.9</span></div>
      <div class="dish-desc">Crispy crepe made with rice and<br>lentil batter stuffed with potatoes</div></div>
    <div class="dish"><div class="dish-name">Udupi Masala Dosa <span class="price">11.9</span></div>
      <div class="dish-desc">Crispy crepe made with rice and lentil<br>batter stuffed with potatoes</div></div>
    <div class="dish"><div class="dish-name">Udupi Masala Dosa <span class="price">11.9</span></div>
      <div class="dish-desc">Crispy crepe made with rice and<br>lentil batter stuffed with potatoes</div></div>
  </div>

  <div class="column right" style="top:794px">
    <div class="dish"><div class="dish-name">Paneer Dosa <span class="price">12.9</span></div>
      <div class="dish-desc">Ricotta cheese mustard seeds<br>chilli curry leaf onion tomato</div></div>
    <div class="dish"><div class="dish-name">Vada Sambar <span class="price">12.9</span></div>
      <div class="dish-desc">Lentil dumpling deep fry</div></div>
    <div class="dish"><div class="dish-name">Paneer Dosa <span class="qty">(2PCS)</span> <span class="price">6.9</span></div>
      <div class="dish-desc">Lentil dumpling deep fry</div></div>
    <div class="dish"><div class="dish-name">Thair Vada <span class="qty">(2PCS)</span> <span class="price">6.9</span></div>
      <div class="dish-desc">Lentil dumpling deep fry in<br>yogurt buttermilk</div></div>
    <div class="dish"><div class="dish-name">Dhai Idly <span class="qty">(2PCS)</span> <span class="price">6.9</span></div>
      <div class="dish-desc">Dumpling made with black lentil rice<br>fermented yogurt</div></div>
    <div class="dish"><div class="dish-name">Vada and Idly Plate <span class="price">8.9</span></div>
      <div class="dish-desc">Lentil and rice dumpling</div></div>
    <div class="dish"><div class="dish-name">Channa Bhtura <span class="qty">(2PCS)</span> <span class="price">10.9</span></div>
      <div class="dish-desc">Chickpeas onion tomato ginger<br>fresh coriander deep fried<br>bread pickle</div></div>
  </div>
</main>
</body>
</html>
```